professional business card design for technology company

We are a small technology consulting firm, specialising in consulting based around Cloud and Managed services. Our colour scheme is yellow, blue and white, as you can see in the logos. Although we are based in melbourne australia, due to the nature of our work, our clients can be located anywhere. We are looking for a clean, professional, positive look - similar to our company logo

Target Market(s)

small business

Industry/Entity Type

Business

Contact Information for Business Card

eye catching, designed to incorporate some level of raised printing. Must contain website address, phone number, name and job title

Requirements
Must have
• Logo (attached) - use of the same colour scheme

```html
<!DOCTYPE html>
<html lang="en">
<head>
<meta charset="utf-8">
<title>Nubivo Business Card</title>
<link rel="stylesheet" href="https://fonts.googleapis.com/css2?family=Arimo:ital,wght@0,400;0,700;1,700&display=swap">
<style>
  :root {
    --blue: #29a8e0;
    --yellow: #ffdc2e;
    --ink: #555555;
    --paper: #ffffff;
    --gap: #c9c9c9;
    --faint-blue: #e3f2fa;
  }
  * { box-sizing: border-box; margin: 0; padding: 0; }
  html, body { width: 1057px; height: 1200px; overflow: hidden; background: var(--gap); }
  body { font-family: "Arimo", Arial, sans-serif; color: var(--ink); position: relative; }

  .card { position: absolute; left: 0; width: 1057px; background: var(--paper); overflow: hidden; }
  .card--front { top: 0; height: 582px; border: 1px solid #9a9a9a; }
  .card--back { top: 613px; height: 587px; border: 1px solid #222; }

  .bar { position: absolute; }
  .bar--yellow { background: var(--yellow); }
  .bar--blue { background: var(--blue); }

  .brand-dot { position: absolute; left: 112px; top: 228px; width: 150px; height: 150px; border-radius: 50%; background: var(--blue); }
  .brand-name { position: absolute; left: 424px; top: 215px; font-size: 172px; font-weight: 700; letter-spacing: -4px; line-height: 1; color: var(--ink); }

  .tagline { position: absolute; left: 0; top: 491px; width: 724px; height: 56px; background: var(--blue); color: var(--paper);
             font-style: italic; font-weight: 700; font-size: 30px; line-height: 56px; padding-left: 42px; }

  .faint-circle { position: absolute; left: 560px; top: 180px; width: 560px; height: 560px; border-radius: 50%; background: var(--faint-blue); }

  .person-name { position: absolute; left: 50px; top: 42px; font-size: 64px; font-weight: 700; line-height: 1; color: var(--ink); }
  .person-title { position: absolute; left: 209px; top: 108px; width: 270px; height: 57px; background: var(--blue); color: var(--paper);
                  font-style: italic; font-weight: 700; font-size: 40px; line-height: 57px; padding-left: 18px; }

  .contact { position: absolute; left: 50px; top: 440px; line-height: 1.05; }
  .contact__phone { font-size: 50px; font-weight: 700; }
  .contact__web { font-size: 52px; font-weight: 400; }
</style>
</head>
<body>
  <section class="card card--front">
    <div class="bar bar--yellow" style="left:435px;top:70px;width:40px;height:59px"></div>
    <div class="bar bar--yellow" style="left:503px;top:70px;width:55px;height:59px"></div>
    <div class="bar bar--yellow" style="left:590px;top:70px;width:84px;height:59px"></div>
    <div class="bar bar--yellow" style="left:705px;top:70px;width:136px;height:59px"></div>
    <div class="bar bar--yellow" style="left:870px;top:70px;width:187px;height:59px"></div>

    <div class="brand-dot"></div>
    <div class="brand-name">Nubivo</div>

    <div class="tagline">Cloud Based Technology Consulting Firm</div>
    <div class="bar bar--blue" style="left:756px;top:491px;width:82px;height:56px"></div>
    <div class="bar bar--blue" style="left:869px;top:491px;width:58px;height:56px"></div>
    <div class="bar bar--blue" style="left:954px;top:491px;width:37px;height:56px"></div>
  </section>

  <section class="card card--back">
    <div class="faint-circle"></div>

    <div class="person-name">FIRST last</div>
    <div class="bar bar--blue" style="left:0;top:108px;width:30px;height:57px"></div>
    <div class="bar bar--blue" style="left:54px;top:108px;width:42px;height:57px"></div>
    <div class="bar bar--blue" style="left:120px;top:108px;width:62px;height:57px"></div>
    <div class="person-title">official title</div>

    <div class="contact">
      <div class="contact__phone">123.456.7890</div>
      <div class="contact__web">Nubivo.com</div>
    </div>
  </section>
</body>
</html>
```